Vellorin - Business Cards for a new venture

create business card for a startup classified business dealing in construction materials, the cards need to have a professional look but modern, more serious than playful, one of the samples must include the official font (attached), please explore using the official colors in the company's logo

Target Market(s)

Energy sector

Contact Information for Business Card

Font styles to use
Other font styles liked:
• suissnord

Requirements
Must have
• corporate colors (in logo attached)
Nice to have
• Official font (in one of the samples) font is : suissnord
Should not have
• Cartoonish look

```html
<!DOCTYPE html>
<html lang="en">
<head>
<meta charset="utf-8">
<title>Vellorin Business Cards</title>
<link href="https://fonts.googleapis.com/css2?family=Open+Sans:wght@400;700;800&display=swap" rel="stylesheet">
<style>
  :root {
    --backdrop: #202020;
    --card: #ffffff;
    --navy: #154a7e;
    --grey: #9a9a9c;
    --ink: #2a2a2a;
  }
  html, body {
    margin: 0;
    width: 1200px;
    height: 1200px;
    overflow: hidden;
    background: var(--backdrop);
    font-family: "Open Sans", sans-serif;
  }
  .card {
    position: absolute;
    left: 182px;
    width: 840px;
    height: 480px;
    background: var(--card);
    overflow: hidden;
  }
  .card--front { top: 94px; }
  .card--back { top: 639px; }
  .card__band-grey,
  .card__band-navy {
    position: absolute;
    left: 0;
    width: 100%;
  }
  .card__band-grey { top: 466px; height: 6px; background: var(--grey); }
  .card__band-navy { top: 472px; height: 8px; background: var(--navy); }

  .wordmark {
    position: absolute;
    display: flex;
    align-items: center;
    gap: 14px;
    transform: translate(-50%, -50%);
    font-weight: 400;
    color: var(--navy);
    letter-spacing: 6px;
    white-space: nowrap;
  }
  .wordmark__square { background: var(--navy); flex: none; }
  .wordmark--front { left: 420px; top: 240px; font-size: 48px; }
  .wordmark--front .wordmark__square { width: 26px; height: 26px; }
  .wordmark--back { left: 244px; top: 240px; font-size: 34px; }
  .wordmark--back .wordmark__square { width: 18px; height: 18px; }

  .notch { position: absolute; top: 207px; width: 24px; height: 58px; }
  .notch--left { left: 0; }
  .notch--right { right: 0; }

  .divider {
    position: absolute;
    left: 434px;
    top: 135px;
    width: 2px;
    height: 216px;
    background: linear-gradient(to bottom, var(--navy) 0 106px, var(--grey) 106px);
  }
  .holder__name {
    position: absolute;
    left: 467px;
    top: 130px;
    margin: 0;
    font-size: 28px;
    font-weight: 800;
    letter-spacing: 1.6px;
    color: var(--navy);
    white-space: nowrap;
  }
  .holder__title {
    position: absolute;
    left: 468px;
    top: 166px;
    margin: 0;
    font-size: 14px;
    color: var(--ink);
    letter-spacing: 0.3px;
  }
  .contact {
    position: absolute;
    left: 464px;
    top: 203px;
    margin: 0;
    padding: 0;
    list-style: none;
  }
  .contact__item {
    display: flex;
    align-items: center;
    height: 31.5px;
    font-size: 17px;
    color: var(--ink);
    letter-spacing: 0.3px;
  }
  .contact__icon { width: 18px; height: 18px; margin-right: 10px; flex: none; }
  .address {
    position: absolute;
    left: 463px;
    top: 313px;
    margin: 0;
    font-style: normal;
    font-size: 16.5px;
    line-height: 20px;
    color: var(--ink);
    letter-spacing: 0.3px;
  }
</style>
</head>
<body>
  <section class="card card--front">
    <div class="wordmark wordmark--front"><span class="wordmark__square"></span>VELLORIN</div>
    <div class="card__band-grey"></div>
    <div class="card__band-navy"></div>
  </section>

  <section class="card card--back">
    <svg class="notch notch--left" viewBox="0 0 24 58"><polygon points="0,0 24,29 0,58" fill="#154a7e"/></svg>
    <svg class="notch notch--right" viewBox="0 0 24 58"><polygon points="24,0 0,29 24,58" fill="#154a7e"/></svg>

    <div class="wordmark wordmark--back"><span class="wordmark__square"></span>VELLORIN</div>

    <div class="divider"></div>

    <h1 class="holder__name">DANIEL HARTLEY</h1>
    <p class="holder__title">ASSOCIATE MANAGER</p>

    <ul class="contact">
      <li class="contact__item">
        <svg class="contact__icon" viewBox="0 0 18 18"><rect x="5" y="1.5" width="8" height="15" rx="1.2" fill="none" stroke="#154a7e" stroke-width="1.3"/><line x1="8" y1="14" x2="10" y2="14" stroke="#154a7e" stroke-width="1.2"/></svg>
        +62-614208735
      </li>
      <li class="contact__item">
        <svg class="contact__icon" viewBox="0 0 18 18"><path d="M2 6 L3.5 2 H14.5 L16 6 Z" fill="none" stroke="#154a7e" stroke-width="1.2"/><rect x="3" y="6" width="12" height="10" fill="none" stroke="#154a7e" stroke-width="1.2"/><rect x="5" y="9" width="3" height="7" fill="none" stroke="#154a7e" stroke-width="1"/><rect x="10" y="9" width="3" height="3" fill="none" stroke="#154a7e" stroke-width="1"/></svg>
        Vellorin office Building
      </li>
      <li class="contact__item">
        <svg class="contact__icon" viewBox="0 0 18 18"><rect x="2" y="5" width="14" height="9" fill="none" stroke="#154a7e" stroke-width="1.2"/><path d="M2 5 L9 10.5 L16 5" fill="none" stroke="#154a7e" stroke-width="1.2"/></svg>
        dhartley@vellorin.co
      </li>
    </ul>

    <address class="address">48/2 HARLOW LANE, EASTFIELD PARK,<br>DENVER, US, 8021940</address>

    <div class="card__band-grey"></div>
    <div class="card__band-navy"></div>
  </section>
</body>
</html>
```